Popular Miami Restaurant & Bar looking for a new ad!!!

We are a high volume restaurant & bar that is constantly running great food and drink specials to keep people coming over and over again. We run ads every week and have been creating them through an ad agency and there ads have gotten to be very boring and bland to me. You can visit our website at www.belvantis.com to see what our menu is like, get our logo and our colors. I will also attach our last ad (which I think looks too busy and boring). I will also attach food pics and our logo. We have an american menu with a good bar crowd, a lot of steaks, chicken, fish and salads. Our clientele is typically a little older and we are starting to do entertainment from Wednesday through Saturday nights. We are going to run a different special everyday of the week as well and want this ad to portray our new specials and entertainment. It will be placed full page in the Coral Ledger, Gulf Coast Daily Courier, Palmetto Gazette and Breezeway Bulletins. We are spending approx. $5,000 a week in advertising and will continue to do so with this new ad.
I would like to see some designs that have a calendar feel to them with the following specials.
Wednesdays: 18 oz Bone In New York Strip with a side for $15.95
with classic oldies and light rock performed by Rollo & Teddy
Thursdays: Filet Mignon Kebob with a side for $15.95 and Marty and Crestones performing Doo Wop all night long.
Fridays: 20 oz T Bone Steak with a side for $15.95 Harwell Bramston Quartet performing Light jazz
Saturdays: 18 oz bone in rib eye with a side for $15.95 with Odalys performing Latin and american hits
Sunday through Tuesday is our 2 for $22 special. Two people come and share an appetizer choose your entree with sides and a dessert to share for only $22!!!
Please email me any questions.
Updates
First placement is a gatefold ad in a newspaper. Dimensions are 4.50" wide x 20" high
The top half of this ad will be the cover of the newspaper so that is the most important piece to use and grab attention.
Industry/Entity Type
Entertainment
Requirements
Must have
- Logo, add Grill and Bar under it.
Address
Phone #
Website
Nice to have
- Attached food shots. These are actual shots of our food taken durning a photo shoot. I think it would be nice that people see these shots of our specials were running.
Some sort of image for the 2 for $22 special.

```html
<!DOCTYPE html>
<html lang="en">
<head>
<meta charset="utf-8">
<title>Belvantis Grill &amp; Bar – Weekly Specials</title>
<link href="https://fonts.googleapis.com/css2?family=Squada+One&family=Oswald:wght@600&family=Roboto+Condensed:wght@400;700&display=swap" rel="stylesheet">
<style>
  :root {
    --brown-dark: #4b2814;
    --brown-mid: #5e331b;
    --tan: #d5b47c;
    --tan-light: #e2c796;
    --maroon: #8a1b2d;
    --cream: #f4e6cc;
    --white: #ffffff;
    --ink: #3f210f;
  }
  * { margin: 0; padding: 0; box-sizing: border-box; }
  html, body { width: 1200px; height: 5337px; overflow: hidden; background: var(--brown-dark); }
  .ad { position: relative; width: 1200px; height: 5337px; overflow: hidden; font-family: "Roboto Condensed", "Arial Narrow", sans-serif; }

  .hero-photo { position: absolute; left: 0; top: 0; width: 1200px; height: 741px;
    background: radial-gradient(ellipse at 45% 55%, #6a2f18 0%, #4a1f10 35%, #d9d4cc 60%, #f3f1ee 80%); }

  .day { position: absolute; left: 0; width: 1200px; }
  .day--dark { background: var(--brown-dark); color: var(--cream); }
  .day--light { background: var(--tan); color: var(--ink); }
  .day--wed { top: 741px; height: 685px; }
  .day--thu { top: 1426px; height: 648px; }
  .day--fri { top: 2074px; height: 686px; }
  .day--sat { top: 2760px; height: 685px; }
  .day--combo { top: 3445px; height: 1892px; background: linear-gradient(#4b2814, #5a2f18 60%, #4b2814); }

  .day__inner { position: absolute; left: 89px; top: 60px; }
  .day--right .day__inner { left: auto; right: 96px; text-align: right; }

  .day__title { font-family: "Squada One", "Impact", sans-serif; font-size: 158px; line-height: 1; letter-spacing: 1px; }
  .day--dark .day__title { color: var(--tan-light); }
  .day--light .day__title { color: var(--ink); }

  .day__dish { font-size: 52px; margin-top: 14px; }
  .day--dark .day__dish { color: var(--tan-light); }

  .day__price { font-family: "Oswald", "Impact", sans-serif; font-weight: 600; font-size: 190px; line-height: 1.05; margin-top: 18px; letter-spacing: -2px; }
  .day--dark .day__price { color: var(--white); }
  .day--light .day__price { color: var(--maroon); }
  .day__price sup { font-size: 0.55em; vertical-align: 0.6em; }

  .day__act { font-size: 40px; line-height: 1.25; margin-top: 14px; }
  .day--dark .day__act { color: var(--white); }
  .day--light .day__act { color: var(--maroon); }
  .day__act strong { font-weight: 700; }

  .dish-photo { position: absolute; border-radius: 50%; }
  .dish-photo--strip { left: 760px; top: 1110px; width: 520px; height: 400px;
    background: radial-gradient(ellipse at 45% 50%, #6b3518 0%, #4d2410 40%, #e9e6e1 62%, #f8f8f6 80%, rgba(248,248,246,0) 82%); }
  .dish-photo--tbone { left: -120px; top: 2593px; width: 530px; height: 444px;
    background: radial-gradient(ellipse at 55% 50%, #6e3419 0%, #4a210f 40%, #e7e3dd 62%, #f8f8f6 80%, rgba(248,248,246,0) 82%); }

  .combo__text { position: absolute; left: 89px; top: 60px; }
  .combo__title { font-family: "Squada One", "Impact", sans-serif; font-size: 158px; color: var(--tan-light); line-height: 1; }
  .combo__copy { font-size: 56px; color: var(--cream); line-height: 1.3; margin-top: 28px; width: 960px; }
  .combo__offer { font-family: "Oswald", "Impact", sans-serif; font-weight: 600; color: var(--white); margin-top: 20px; line-height: 1; }
  .combo__offer .small { font-size: 80px; }
  .combo__offer .big { font-size: 170px; }

  .combo-photo { position: absolute; left: 0; top: 4110px; width: 1200px; height: 760px;
    background: radial-gradient(ellipse at 50% 45%, rgba(120,55,25,0.85) 0%, rgba(80,35,15,0.6) 45%, rgba(75,40,20,0) 75%); }

  .brand { position: absolute; left: 0; width: 1200px; text-align: center; color: var(--white); }
  .brand__web { top: 4715px; font-size: 52px; color: var(--cream); }
  .brand__name { top: 4785px; font-size: 200px; font-weight: 400; line-height: 1; }
  .brand__sub { top: 5010px; font-size: 100px; font-weight: 400; }
</style>
</head>
<body>
<main class="ad">
  <div class="hero-photo" role="img" aria-label="Grilled bone-in steak on a white plate with broccoli and carrots"></div>

  <section class="day day--dark day--wed">
    <div class="day__inner">
      <h2 class="day__title">Wednesdays</h2>
      <p class="day__dish">18oz Bone In New York Strip with a side</p>
      <p class="day__price"><sup>$</sup>15.95</p>
      <p class="day__act">with classic oldies and light rock<br>performed by <strong>Rollo &amp; Teddy</strong></p>
    </div>
  </section>

  <section class="day day--light day--thu">
    <div class="day__inner">
      <h2 class="day__title">Thursdays</h2>
      <p class="day__dish">Filet Mignon Kebob with a side</p>
      <p class="day__price"><sup>$</sup>15.95</p>
      <p class="day__act"><strong>Marty and Crestones</strong><br>performing Doo Wop all night long</p>
    </div>
  </section>

  <section class="day day--dark day--right day--fri">
    <div class="day__inner">
      <h2 class="day__title">Fridays</h2>
      <p class="day__dish">20 oz T Bone Steak with a side</p>
      <p class="day__price"><sup>$</sup>15.95</p>
      <p class="day__act"><strong>Harwell Bramston Quartet</strong> performing Light jazz</p>
    </div>
  </section>

  <section class="day day--light day--right day--sat">
    <div class="day__inner">
      <h2 class="day__title">Saturdays</h2>
      <p class="day__dish">18 oz bone in rib eye with a side</p>
      <p class="day__price"><sup>$</sup>15.95</p>
      <p class="day__act"><strong>Odalys</strong> performing Latin and american hits</p>
    </div>
  </section>

  <div class="dish-photo dish-photo--strip" role="img" aria-label="New York strip steak with asparagus on a plate"></div>
  <div class="dish-photo dish-photo--tbone" role="img" aria-label="Grilled T-bone steak on a plate"></div>

  <section class="day day--combo">
    <div class="combo__text">
      <h2 class="combo__title">Sunday – Tuesday</h2>
      <p class="combo__copy">Two people come and share<br>an appetizer choose your entree<br>with sides and a dessert to share</p>
      <p class="combo__offer"><span class="small">2 for </span><span class="big">$22 special</span></p>
    </div>
  </section>

  <div class="combo-photo" role="img" aria-label="Close-up of a seasoned grilled steak fading into the background"></div>

  <p class="brand brand__web">www.belvantis.com</p>
  <p class="brand brand__name">Belvantis</p>
  <p class="brand brand__sub">Grill &amp; Bar</p>
</main>
</body>
</html>
```